FREE BBQ for life if you win our business with your creative menu design

Looking for a 11x17 size menu. we are a full service BBQ restaurant. We have an upscale environment as well as up scale service. We offer 5 star dinning at a casual price. we are on route 66 and are proud of that. we offer the finest smoked meats. Specializing in smoked pork beef and bison. we have an old barn wood decor. we only use oak to smoke our meats. use a lot of tarnished metal as well as some string nail art. Looking for a menu that goes along our style. i have attached as many pictures as i could to give you a fill of how we do it out here.
PLEASE USE THE 11"X17" MENU TEMPLATE ATTACHED IN THE PROJECT BRIEF.
Target Market(s)
Cool people and there families.
Industry/Entity Type
Business
Requirements
Must have
- I have attached the Current menu we use. File morvays menu pub. Those are all the Items. There will be some changes as we but together the new menu. The prices are changing. but that should be an easy change as we go.
Nice to have
- We are getting away from the lunch dinner menu and going to an all day menu. so rather than coming with toast or bun we will now be asking as an option. I have attached a menu i tried to make as a sample of how we will be doing it. new menu single page and new menu single page flame. These are ideas i had but could not really make it work. so use them as an idea of what we are looking for but be creative.

```html
<!DOCTYPE html>
<html lang="en">
<head>
<meta charset="utf-8">
<title>Morvays Barbeque Menu</title>
<link rel="stylesheet" href="https://fonts.googleapis.com/css2?family=PT+Sans:ital,wght@0,400;0,700;1,400;1,700&display=swap">
<style>
:root{
  --stage:#2b2b2b;
  --wood-dark:#2a1b12;
  --wood-mid:#4a3322;
  --wood-light:#5c4029;
  --band:#1d130d;
  --plaque:#3a2718;
  --heading:#e6cfae;
  --item:#f3e6d2;
  --body:#d8c6ad;
  --herb:#5f8a3a;
  --plate:#a3563e;
}
*{box-sizing:border-box;margin:0;padding:0}
html,body{width:1200px;height:993px;overflow:hidden;background:var(--stage)}
body{font-family:"PT Sans",sans-serif;position:relative}
.menu{
  position:absolute;left:290px;top:16px;width:620px;height:960px;
  background:linear-gradient(90deg,var(--wood-dark) 0%,var(--wood-mid) 22%,var(--wood-light) 45%,var(--wood-mid) 70%,var(--wood-dark) 100%);
  overflow:hidden;
}
.menu-header{
  height:70px;background:var(--band);
  display:flex;align-items:center;justify-content:center;
}
.brand-plaque{
  background:var(--plaque);padding:8px 22px;border-radius:3px;
}
.brand-name{font-weight:700;font-size:20px;color:var(--heading);letter-spacing:1px;text-transform:uppercase}
.columns{display:flex;gap:20px;padding:12px 26px 0 26px;height:740px}
.col{flex:1;overflow:hidden}
.section-title{
  font-weight:700;font-size:20px;color:var(--heading);text-align:center;
  letter-spacing:1px;margin:6px 0 3px;text-transform:uppercase;
}
.note{font-style:italic;font-size:9px;color:var(--body);line-height:1.25}
.note.strong{font-weight:700;color:var(--item)}
.item{margin-top:3px}
.item-name{font-weight:700;font-size:9.5px;color:var(--item);line-height:1.2}
.item-desc{font-size:9px;color:var(--body);line-height:1.25}
.price{font-style:italic}
.drinks-row{display:flex;justify-content:space-between;padding:2px 6px 0}
.herb{position:absolute;left:24px;bottom:28px;width:110px;height:60px;background:radial-gradient(ellipse at center,var(--herb) 0%,rgba(95,138,58,0.2) 70%,transparent 100%)}
.dish{position:absolute;right:22px;bottom:20px;width:270px;height:112px;border-radius:140px 140px 0 0;background:radial-gradient(circle at 50% 75%,var(--plate) 0%,#6b4a3a 50%,#c9c5c0 80%,#8d8985 100%)}
.footer{position:absolute;left:0;right:0;bottom:0;height:18px;background:var(--band);font-size:7.5px;color:var(--body);text-align:center;line-height:18px}
</style>
</head>
<body>
<main class="menu">
  <header class="menu-header">
    <div class="brand-plaque"><span class="brand-name">Morvays Barbeque</span></div>
  </header>

  <div class="columns">
    <section class="col">
      <h2 class="section-title">Bison</h2>
      <p class="note strong">Heart Healthy</p>
      <p class="note">Served with 1 sides and your choice of Texas toast, Kaiser bun, or Gluten Free bread</p>
      <div class="item"><p class="item-name">Bison Brisket</p><p class="item-desc">The belly of beast, smoked then sliced thin and grilled. Juicy and tender 18.65</p></div>
      <div class="item"><p class="item-name">Bison Burger</p><p class="item-desc">Smoked then grilled served with pepper jack cheese lettuce tomato pickle topped with spicy ranch. 12.59</p></div>
      <div class="item"><p class="item-name">Bison Steak</p><p class="item-desc">12oz of lean healthy meat cooked to your desired temp. 34.56</p></div>

      <h2 class="section-title">Smoked</h2>
      <p class="note">Served with 1 sides and your choice of Texas toast, Kaiser bun, or Gluten Free bread</p>
      <div class="item"><p class="item-name">Baby Back Ribs</p><p class="item-desc">Tender to the bone, finger licking good, never need a knife, best ribs you'll ever have. <span class="price">Full Rack 22.59 Half Rack 12.49</span></p></div>
      <div class="item"><p class="item-name">St. Louis Ribs</p><p class="item-desc">A nice big tender rib, slow smoked, so tender that you can sink your teeth into. <span class="price">Half 16.45 Full 30.89</span></p></div>
      <div class="item"><p class="item-name">Beef Brisket</p><p class="item-desc">The most insane mouth watering smoky, moist, succulent piece of meat your mouth will ever have. 10.95</p></div>
      <div class="item"><p class="item-name">Pulled Pork</p><p class="item-desc">Smoked for 18-20 hrs, then pulled and mixed with our signature base barbeque sauce. 9.59</p></div>
      <div class="item"><p class="item-name">Sliced Pork</p><p class="item-desc">Smoked juicy tenderloin sliced thin then grilled per order. 10.54</p></div>
      <div class="item"><p class="item-name">Smoked Turkey</p><p class="item-desc">Breast meat smoked and sliced. Juicy and tender. 11.49</p></div>
      <div class="item"><p class="item-name">Smoked Chicken Half</p><p class="item-desc">Moist and juicy smoked breast and thigh on the bone basted with our signature sauce on the grill. 13.59</p></div>
      <div class="item"><p class="item-name">Rib Eye</p><p class="item-desc">12oz juicy steak grilled to your desired temp 21.95<br><span class="price">All meats are Gluten free. Please specify if you are gluten intolerant.</span></p></div>

      <h2 class="section-title">MB Customs</h2>
      <p class="note">Served with 1 sides</p>
      <div class="item"><p class="item-name">BBQ Tacos</p><p class="item-desc">Three Tacos in blue and red shells with your choice of meat topped with shredded lettuce and Pico-D-BBQ and Spicy ranch. (Excludes ribs and bison). 9.89<br>Taco Tuesday is a Must! 5.00 tacos all day</p></div>
      <div class="item"><p class="item-name">Rowdy Chicken Sandwich</p><p class="item-desc">Skinless boneless chicken breast, breaded and fried, topped with pepper jack cheese, spicy ranch, lettuce, tomato onion and pickles. On buttery grilled Texas toast. 10.59</p></div>
      <div class="item"><p class="item-name">Wrap it</p><p class="item-desc">Take any Meat and ask your server to wrap it! Comes with the meat you choose topped cheese, lettuce, Pico-D-BBQ and spicy ranch.</p></div>
    </section>

    <section class="col">
      <h2 class="section-title">Appetizers</h2>
      <div class="item"><p class="item-name">King Rings</p><p class="item-desc">Green Chili battered fried golden crispy 1" thick onion rings. Served with spicy ranch. 7.89</p></div>
      <div class="item"><p class="item-name">Deep Fried Pickles</p><p class="item-desc">Crisp dill pickle chips battered and fried to a golden crispy brown. Served with spicy ranch. 7.89</p></div>
      <div class="item"><p class="item-name">Fried Okra</p><p class="item-desc">Okra is breaded then fried until golden. Served with spicy ranch. 7.89</p></div>
      <div class="item"><p class="item-name">Green Chili Waffle Fries</p><p class="item-desc">Crispy waffle-cut fries, topped with a savory blend of cheese, and New Mexico green chile. Served with spicy ranch. 7.89</p></div>
      <div class="item"><p class="item-name">MB Wild Wings</p><p class="item-desc">Big, meaty pork wings, deep fried to a perfect golden brown, tossed in a hot Buffalo-style sauce, and served with spicy buttermilk ranch dressing on the side. Served with spicy ranch. 8.99</p></div>
      <div class="item"><p class="item-name">Sample Platter</p><p class="item-desc">Two MB Wild Wings, 6oz of Fried Pickles, 6oz of King Rings. Served with spicy ranch. 8.59</p></div>

      <h2 class="section-title">Sides</h2>
      <p class="item-desc">Green Chile Creamed Corn | Potato Salad | Baked Potato<br>Grilled Veggie | Baked Bean | Waffle Fries | Coleslaw<br><span class="price">Extra side 2.29</span></p>

      <h2 class="section-title">Deserts</h2>
      <div class="item"><p class="item-name">Peach Cobbler &amp; Icecream</p><p class="item-desc">Served hot topped with ice cream. <span class="price">large 5.89 Small 3.2</span></p></div>
      <div class="item"><p class="item-name">Cookies A-L-Mode</p><p class="item-desc">Hot gooey cookies topped with ice cream your choice chocolate chip or macadamia nut. large 5.89 Small 3.29</p></div>
      <div class="item"><p class="item-name">Desert Of The Week</p><p class="item-desc">Ask your server for our special dessert of the week</p></div>

      <h2 class="section-title">Drinks</h2>
      <div class="item"><p class="item-name">Lemonade</p><p class="item-desc">Regular | Strawberry | Watermelon | Cherry | Peach <span class="price">2.59</span></p></div>
      <div class="item"><p class="item-name">Fountains</p><p class="item-desc">Fizz Cola | Doc Spice | Root Beer | Lemon Breeze | Citrus Peak<br>Diet Fizz Cola | Diet Doc Spice <span class="price">1.89</span></p></div>
      <div class="drinks-row">
        <div><p class="item-name">Iced Teas</p><p class="item-desc price">1.89</p></div>
        <div><p class="item-name">Coffee</p><p class="item-desc price">2.69</p></div>
        <div><p class="item-name">Hot Chocolate</p><p class="item-desc price">2.89</p></div>
      </div>

      <h2 class="section-title">Salads</h2>
      <div class="item"><p class="item-name">All You Can Eat Salad Bar</p><p class="item-desc">Enjoy as much salad as you would like. 7.89</p></div>
      <div class="item"><p class="item-name">Meaty Salad</p><p class="item-desc">Choose any meat to add to your salad 3oz of meat. (Excludes ribs and bison) 3.00</p></div>
      <div class="item"><p class="item-name">Side Salad</p><p class="item-desc">With out meal 3.00<br>Add to meal 1.50</p></div>
    </section>
  </div>

  <div class="herb" role="img" aria-label="Photo of fresh green herb leaves"></div>
  <div class="dish" role="img" aria-label="Photo of a plated grilled steak with potatoes and greens"></div>
  <footer class="footer">Ask about our catering and private events. Smoked fresh daily with oak on Route 66.</footer>
</main>
</body>
</html>
```